Sandwich Board and Poster design promoting a medical aesthetic clinic

I am looking for a clean, modern and relaxing design promoting a medical physician-led aesthetic clinic.
Services offered are neuromodulator treatment (Quelvo) and Dermal Fillers.
Logo must be included.
Use the tag line "Refresh your look, revive your spirit."
Address is 204-205 27361 92 Ave, Surrey, V7K 2M4
604-555-0148
email - info@lumawellpine.ca
www.lumawellpine.ca

```html
<!DOCTYPE html>
<html lang="en">
<head>
<meta charset="utf-8">
<title>Lumawell Pine – Sandwich Board &amp; Poster</title>
<link rel="stylesheet" href="https://fonts.googleapis.com/css2?family=Montserrat:wght@500&family=Oswald:wght@400&family=Poppins:ital,wght@0,600;1,600&family=Syne:wght@700&display=swap">
<style>
  :root {
    --paper: #ffffff;
    --ink: #1e1b1c;
    --gold: #e2bb2e;
    --gold-mid: #c9a42c;
    --gold-deep: #ad8a30;
    --photo-warm: #c9a487;
    --photo-dark: #3a2a22;
    --mist: #eef0f3;
  }
  * { margin: 0; padding: 0; box-sizing: border-box; }
  html, body { width: 880px; height: 1200px; overflow: hidden; background: var(--paper); }
  .poster { position: relative; width: 880px; height: 1200px; background: var(--paper); }

  .size-note {
    position: absolute; top: 32px; left: 0; width: 880px; text-align: center;
    font: italic 600 22px/1 "Poppins", sans-serif; color: var(--ink);
  }

  .photo { position: absolute; top: 120px; height: 368px; width: 198px; }
  .photo--left {
    left: 95px;
    background: linear-gradient(180deg, var(--photo-dark) 0%, var(--photo-warm) 30%, #e6d2c3 53%, var(--mist) 60%, var(--paper) 100%);
  }
  .photo--right {
    left: 589px;
    background: linear-gradient(180deg, #d8c3a0 0%, var(--photo-warm) 20%, #8a6450 40%, #e6d6ca 53%, var(--mist) 60%, var(--paper) 100%);
  }

  .brand-name {
    position: absolute; top: 366px; left: 0; width: 880px; text-align: center;
    font: 500 40px/1 "Montserrat", sans-serif; letter-spacing: 0.32em;
    color: var(--ink); padding-left: 0.32em;
  }

  .tagline { position: absolute; top: 0; left: 0; width: 880px; height: 0; }
  .tagline__side {
    position: absolute; top: 522px; display: flex; flex-direction: column;
    font: 700 40px/38px "Syne", sans-serif; color: var(--gold-mid);
  }
  .tagline__side--left { left: 95px; width: 235px; text-align: right; }
  .tagline__side--right { left: 610px; width: 170px; text-align: left; }
  .tagline__your {
    position: absolute; top: 506px; left: 336px; width: 264px; text-align: center;
    font: 600 98px/1 "Poppins", sans-serif; letter-spacing: -3px; color: var(--gold);
  }

  .service {
    position: absolute; font: 400 36px/1 "Oswald", sans-serif; white-space: nowrap;
  }
  .service--fillers { left: 117px; top: 722px; color: var(--gold-deep); }
  .service--neuro { left: 350px; top: 672px; color: var(--gold); }

  .service-band {
    position: absolute; left: 95px; top: 770px; width: 692px; height: 134px;
    background: linear-gradient(90deg, var(--gold-deep) 0%, var(--gold-deep) 30%, var(--gold) 55%, var(--gold) 100%);
  }

  .contact { list-style: none; }
  .contact__row { position: absolute; left: 95px; display: flex; align-items: flex-start; }
  .contact__icon {
    width: 54px; height: 34px; background: var(--gold-deep);
    display: flex; align-items: center; justify-content: center; flex-shrink: 0;
  }
  .contact__text {
    margin-left: 12px; margin-top: -4px; font: 600 31px/38px "Poppins", sans-serif;
    color: var(--ink); white-space: nowrap;
  }
</style>
</head>
<body>
<main class="poster">
  <p class="size-note">Sandwich Board and Poster design size are the same 24” x 36”</p>

  <div class="photo photo--left" role="img" aria-label="Profile portraits of two women facing right, with a soft reflection fading below"></div>
  <div class="photo photo--right" role="img" aria-label="Profile portraits of two women facing left, with a soft reflection fading below"></div>

  <h1 class="brand-name">LUMAWELL PINE</h1>

  <h2 class="tagline" aria-label="Refresh your look, revive your spirit">
    <span class="tagline__side tagline__side--left"><span>Refresh</span><span>Revive</span></span>
    <span class="tagline__your">YOUR</span>
    <span class="tagline__side tagline__side--right"><span>Look</span><span>Spirit</span></span>
  </h2>

  <p class="service service--neuro">NEUROMODULATOR TREATMENT</p>
  <p class="service service--fillers">DERMAL FILLERS</p>
  <div class="service-band" role="img" aria-label="Flowing gold wave graphic in deep and bright gold"></div>

  <ul class="contact">
    <li class="contact__row" style="top:924px">
      <span class="contact__icon">
        <svg width="18" height="22" viewBox="0 0 18 22"><path fill="#fff" d="M9 0C4 0 0 4 0 9c0 6 9 13 9 13s9-7 9-13c0-5-4-9-9-9zm0 12a3 3 0 110-6 3 3 0 010 6z"/></svg>
      </span>
      <span class="contact__text">204-205 27361 92 Ave, Surrey,<br>V7K 2M4</span>
    </li>
    <li class="contact__row" style="top:1011px">
      <span class="contact__icon">
        <svg width="22" height="22" viewBox="0 0 24 24"><path fill="#fff" d="M6.6 10.8a15 15 0 006.6 6.6l2.2-2.2c.3-.3.7-.4 1-.2 1.1.4 2.3.6 3.6.6.6 0 1 .4 1 1V20c0 .6-.4 1-1 1C10.6 21 3 13.4 3 4c0-.6.4-1 1-1h3.5c.6 0 1 .4 1 1 0 1.3.2 2.5.6 3.6.1.3 0 .7-.2 1z"/></svg>
      </span>
      <span class="contact__text">604-555-0148</span>
    </li>
    <li class="contact__row" style="top:1054px">
      <span class="contact__icon">
        <svg width="22" height="22" viewBox="0 0 24 24"><circle cx="12" cy="12" r="4" fill="none" stroke="#fff" stroke-width="2"/><path d="M16 8v5a3 3 0 006 0v-1a10 10 0 10-4 8" fill="none" stroke="#fff" stroke-width="2"/></svg>
      </span>
      <span class="contact__text">info@lumawellpine.ca</span>
    </li>
    <li class="contact__row" style="top:1097px">
      <span class="contact__icon">
        <svg width="22" height="22" viewBox="0 0 24 24" fill="none" stroke="#fff" stroke-width="1.6"><circle cx="12" cy="12" r="10"/><ellipse cx="12" cy="12" rx="4.5" ry="10"/><path d="M2 12h20M4 6.5h16M4 17.5h16"/></svg>
      </span>
      <span class="contact__text">www.lumawellpine.ca</span>
    </li>
  </ul>
</main>
</body>
</html>
```